Premium Personal Brand — Facebook Banner (Used Across All Platforms)

Update — Additional Color Direction
In addition to the dark charcoal/slate direction already described, I'm also interested in seeing variants with:
Dark navy blue — Deep, authoritative, intelligence-community feel. Same textured/matte treatment, not flat or bright.
Warm charcoal with steel blue accent — Keep the dark base but introduce a subtle steel blue gradient, accent line, or tonal shift. Sophisticated, modern, adds dimension without adding color noise.
Both should maintain the same premium, restrained, architectural feel described in the original brief. No bright blues, no corporate PowerPoint energy — think midnight, think depth, think weight.
Everything else in the brief remains the same.
I am building a premium personal brand as an executive advisor to founders ($5M+ revenue).
This contest is Facebook-banner–focused, but the design must represent a visual system that will be reused across:
- LinkedIn
- YouTube
I- nstagram
- X (Twitter)
- Website hero sections and other brand touchpoints
Think of the Facebook banner as the primary expression of the brand — not a one-off graphic.
This project is about discovering a high-end visual style and brand feel, not decoration.
What to design
Please submit one cohesive visual system, shown primarily as:
- Facebook banner (primary focus)
The same design language should clearly translate to all platforms listed above.
Designers are responsible for using the current recommended dimensions for each platform.
Quick clarification on background direction:
Backgrounds should have depth and texture, not flat color fields. Avoid pure white, light grey, or solid black backgrounds. Think matte, architectural materials — stone, graphite, concrete, steel — not blank canvases. Subtle tonal variation is encouraged. Obvious gradients or decorative patterns are not.
Text to use
Primary Headline:
- Your Business Is Too Valuable To Be Run On Hope.
Subheadline:
- You didn’t build a business to become its prisoner.
Name:
Paul Whitaker
The headline should be the dominant visual element.
Logo note (important)
My personal logo is currently being finalized.
For this contest:
- Use a simple “PW” monogram placeholder
- Clean, bold, geometric sans-serif
- Do not design a logo
- The winning design must allow an easy logo swap later.
Headshot note (important)
- Please do not include a headshot in the banner design.
- Most platforms display a circular profile image separately.
- The banner should stand on its own using typography, layout, and tone only.
- Design the banner assuming the profile photo will sit nearby, not inside the banner.
Style direction
The design should feel:
- Premium
- Calm
- Confident
- Restrained
- High-trust
- Dark, neutral backgrounds are preferred.
- Fewer elements are better than more.
Think:
- Owner-level advisor
- Private equity / boardroom tone
- Industrial, Modern, Minimalist, Elite, Architectural, not decorative
What to avoid
Please do not submit designs that feel:
- Promotional, hype-driven, or salesy
- Like a coach, guru, or agency
- Bright, colorful, or gradient-heavy
- Busy or over-designed
- Based on stock photos
- No motivational speaker energy.
Reaction test
- If someone sees this banner on Facebook (or later on LinkedIn, YouTube, etc.), the reaction should be:
“That person is serious. I’d trust them with important decisions.”
Final note
- I am not looking for many variations.
- I am looking for one strong visual direction you believe in.
Simple beats clever.
- Restraint beats decoration.

```html
<!DOCTYPE html>
<html lang="en">
<head>
<meta charset="utf-8">
<title>Paul Whitaker — Facebook Banner</title>
<link rel="stylesheet" href="https://fonts.googleapis.com/css2?family=Orbitron:wght@600;700&family=Russo+One&family=Saira+Semi+Condensed:wght@500&family=Montserrat:wght@500&display=swap">
<style>
  :root {
    --page: #1a2223;
    --deep: #060b0d;
    --teal-dark: #0c2a2c;
    --teal: #155a5a;
    --slate: #4a5a60;
    --mint: #bfe3dc;
    --white: #f2f6f5;
    --line: rgba(225, 240, 236, 0.75);
    --corner: #1f4a4e;
  }
  html, body {
    margin: 0;
    width: 1200px;
    height: 849px;
    overflow: hidden;
    background: var(--page);
  }
  .banner {
    position: absolute;
    left: 0;
    top: 161px;
    width: 1200px;
    height: 527px;
    overflow: hidden;
    color: var(--white);
  }
  .banner__backdrop {
    position: absolute;
    inset: 0;
    background:
      radial-gradient(ellipse 260px 140px at 470px 40px, rgba(120, 135, 142, 0.55), transparent 70%),
      radial-gradient(ellipse 300px 180px at 1130px 90px, rgba(25, 110, 105, 0.7), transparent 70%),
      radial-gradient(ellipse 420px 200px at 180px 120px, rgba(40, 90, 95, 0.6), transparent 75%),
      linear-gradient(165deg, var(--teal-dark) 0%, #0b1a1e 45%, var(--deep) 70%, #0d2628 100%);
  }
  .banner__frame { position: absolute; inset: 0; }
  .monogram {
    position: absolute;
    left: 54px;
    top: 52px;
    width: 49px;
    height: 49px;
    border: 2px solid var(--white);
    border-radius: 7px;
    display: flex;
    align-items: center;
    justify-content: center;
    font-family: "Russo One", sans-serif;
    font-size: 19px;
    color: var(--white);
  }
  .headline {
    position: absolute;
    left: 296px;
    top: 160px;
    width: 607px;
    margin: 0;
    font-weight: normal;
  }
  .headline__lead,
  .headline__tail {
    display: block;
    font-family: "Saira Semi Condensed", sans-serif;
    font-weight: 500;
    font-size: 34px;
    line-height: 1;
    color: var(--white);
    text-shadow: 0 3px 6px rgba(0, 0, 0, 0.6);
  }
  .headline__key {
    display: block;
    margin-top: 4px;
    font-family: "Russo One", sans-serif;
    font-size: 110px;
    line-height: 0.8;
    letter-spacing: -1px;
    color: var(--mint);
    text-shadow: 0 4px 8px rgba(0, 0, 0, 0.55);
  }
  .headline__tail {
    margin-top: 8px;
    text-align: right;
  }
  .subheadline {
    position: absolute;
    left: 294px;
    top: 340px;
    width: 612px;
    margin: 0;
    font-family: "Montserrat", sans-serif;
    font-weight: 500;
    font-size: 11px;
    letter-spacing: 5.6px;
    white-space: nowrap;
    color: var(--white);
  }
  .signature {
    position: absolute;
    right: 55px;
    top: 452px;
    margin: 0;
    font-family: "Orbitron", sans-serif;
    font-weight: 700;
    font-size: 23px;
    letter-spacing: 2px;
    color: var(--white);
  }
</style>
</head>
<body>
  <section class="banner">
    <div class="banner__backdrop" role="img" aria-label="Flowing dark teal silk texture"></div>
    <svg class="banner__frame" width="1200" height="527" viewBox="0 0 1200 527" aria-hidden="true">
      <line x1="76.5" y1="137" x2="76.5" y2="527" stroke="var(--line)" stroke-width="1.5"/>
      <line x1="1145.5" y1="0" x2="1145.5" y2="433" stroke="var(--line)" stroke-width="1.5"/>
      <polygon points="1096,527 1200,422 1200,527" fill="var(--corner)"/>
    </svg>
    <div class="monogram">PW</div>
    <h1 class="headline">
      <span class="headline__lead">YOUR BUSINESS IS TOO</span>
      <span class="headline__key">VALUABLE</span>
      <span class="headline__tail">TO BE RUN ON HOPE</span>
    </h1>
    <p class="subheadline">YOU DIDN'T BUILD A BUSINESS TO BECOME ITS PRISONER</p>
    <p class="signature">PAUL WHITAKER</p>
  </section>
</body>
</html>
```